WP website design (Carrowind)

We need a wordpress design for an established auction and real estate company based in Florida. The winning design will incorporate a professional color scheme with company logo in a clean layout. The design needs to consider that this will be developed on a responsive theme. Colors are those that will highlight the logo.

Industry/Entity Type

Real Estate

Font styles to use
Serif
Sans Serif

Colors

Designer to choose colors to be used in the design.

Requirements
Must have
• Navigation:
1) Home
2) Auctions
3) Online Auctions
4) About Us
5) Services
6) Real Estate Listings
7) References
8) Contact Us

Colors will be blue (#000066) / red (#B10000) and black or other complementary color. Tagline to be used "Since 1977, Proven Results." Slideshow to be placed in the header or body of home page - please use stock real estate image.

Widgets: 1) Email Sign-up 2) Social media icons for Chirpa and TradeLoop 3) Featured Listings 4) Testimonials 5) Register button

Footer will have smaller company logo, attached logos and contact info:
Phone: (555) 218-6049 Mobile: (555) 762-3815
Email: marlacarrowind@plexmail.example
Address: 48 E. Thornbury Lane, Ste 310, Pensacola, FL 32599
Nice to have
• Use of a drop down menu:
Auctions-
1) Upcoming Auctions
2) Past Auctions

```html
<!DOCTYPE html>
<html lang="en">
<head>
<meta charset="utf-8">
<title>Carrowind Auctions</title>
<link href="https://fonts.googleapis.com/css2?family=Lato:ital,wght@0,400;0,700;1,400&display=swap" rel="stylesheet">
<style>
:root{
  --blue:#2e3192;
  --red:#d9202e;
  --ink:#333;
  --muted:#888;
  --grey-bg:#efefef;
  --line:#dcdcdc;
  --white:#fff;
}
*{box-sizing:border-box;margin:0;padding:0}
html,body{width:977px;height:1200px;overflow:hidden}
body{position:relative;background:var(--white);font-family:'Lato',sans-serif;color:var(--ink)}
.abs{position:absolute}
.top-rule{left:0;top:0;width:977px;height:2px;background:var(--blue)}

.brand{left:128px;top:30px;display:flex;align-items:center;gap:12px}
.brand-mark{width:44px;height:44px;background:var(--blue)}
.brand-name{font-size:27px;font-weight:700;color:var(--blue);letter-spacing:.3px;white-space:nowrap}

.follow{left:478px;top:40px}
.label{font-size:10px;color:var(--muted);white-space:nowrap}
.social{display:flex;gap:9px;margin-top:8px}
.social-item{display:flex;align-items:center;gap:5px;font-size:10.5px;font-weight:700;color:var(--blue);white-space:nowrap}
.social-sq{width:14px;height:14px;background:var(--blue)}
.divider-v{width:1px;height:46px;background:var(--line)}
.contact-block{top:44px}
.contact-block .label{display:flex;align-items:center;gap:5px}
.contact-value{margin-top:8px;color:var(--red);font-size:10.5px;white-space:nowrap}
.contact-value.phone{font-size:12px}

.main-nav{left:0;top:112px;width:977px;height:42px;background:var(--blue)}
.nav-item{top:0;height:42px;line-height:42px;color:var(--white);font-size:12px;white-space:nowrap}
.nav-item.active{background:var(--red);padding:0 18px}
.dropdown{left:176px;top:154px;width:178px;background:var(--red);z-index:3}
.dropdown div{height:32px;line-height:32px;padding-left:16px;font-size:11px;color:var(--white);border-bottom:1px solid rgba(0,0,0,.12)}
.dropdown div.dim{color:rgba(255,255,255,.75);border:0}

.hero{left:0;top:154px;width:977px;height:296px;background:linear-gradient(135deg,#c9c2ad 0%,#b7b59c 100%)}
.slide-arrow{width:30px;height:30px;background:rgba(0,0,0,.45);top:306px;display:flex;align-items:center;justify-content:center}

.tagline-band{left:0;top:450px;width:977px;height:100px;background:var(--red);color:var(--white)}
.tagline{left:130px;top:14px;font-size:23px;font-weight:700;white-space:nowrap}
.tagline-copy{left:131px;top:46px;width:470px;font-size:9.3px;line-height:15px;font-weight:700}
.btn{display:flex;align-items:center;justify-content:center;color:var(--white);font-size:12px;white-space:nowrap}
.btn-register{left:616px;top:40px;width:234px;height:31px;background:var(--blue)}

.featured{left:130px;top:580px;width:472px;height:176px;border:1px solid var(--line)}
.featured-photo{left:14px;top:12px;width:94px;height:98px;background:linear-gradient(180deg,#c7cdd0 0%,#a9aea2 100%);border:2px solid #e6e6e6}
.photo-tools{left:14px;top:110px;width:94px;height:22px;background:var(--blue);display:flex;justify-content:space-around;align-items:center}
.btn-bidding{left:14px;top:141px;width:94px;height:24px;background:var(--red);font-size:10px;border-radius:2px}
.feat-title{left:123px;top:10px;font-size:14px}
.feat-desc{left:123px;top:32px;width:330px;font-size:9.5px;line-height:13px;color:var(--muted)}
.feat-loc{left:123px;top:74px;font-size:7.5px;color:var(--muted);display:flex;gap:6px;align-items:center}
.feat-box{left:124px;top:89px;width:333px;height:75px;border:1px solid var(--line)}
.feat-online{left:11px;top:9px;font-size:9.5px;color:var(--muted)}
.feat-live{left:167px;top:-1px;width:166px;height:23px;background:var(--blue);font-size:9.5px}
.feat-dates{left:11px;top:36px;font-size:9.5px;line-height:17px;color:var(--muted)}

.testimonials-title{left:618px;top:586px;font-size:14px}
.quote-box{left:617px;top:614px;width:231px;height:84px;background:var(--grey-bg);padding:16px 16px 0 16px;font-size:9px;line-height:15px;font-style:italic;color:var(--muted)}
.author{left:620px;top:710px;font-size:11px}
.author-role{left:620px;top:726px;font-size:8.5px;color:var(--muted)}
.dots{left:804px;top:711px;display:flex;gap:5px}
.dots span{width:6px;height:6px;border-radius:50%;background:#bbb}
.dots span.on{background:var(--blue)}

.partner{top:808px;height:44px;background:#e2e2e2;border-radius:3px}

.newsletter{left:0;top:872px;width:977px;height:114px;background:var(--grey-bg)}
.news-title{left:0;top:18px;width:977px;text-align:center;font-size:14px}
.news-sub{left:0;top:40px;width:977px;text-align:center;font-size:9.5px;color:var(--muted)}
.field{top:66px;width:232px;height:30px;background:var(--white);border:1px solid var(--line);font-size:10px;color:var(--muted);padding-left:11px;display:flex;align-items:center;justify-content:space-between;padding-right:10px}
.btn-signup{left:614px;top:66px;width:234px;height:30px;background:var(--red);font-size:10.5px}

.foot-h{top:1005px;font-size:13.5px}
.foot-text{left:130px;top:1036px;width:210px;font-size:9.5px;line-height:16px;color:var(--muted)}
.foot-social{left:128px;top:1096px;display:flex;gap:14px}
.foot-link{font-size:9.5px;color:var(--muted);display:flex;align-items:center;gap:6px;white-space:nowrap}
.foot-link::before{content:"";border-left:4px solid #555;border-top:3px solid transparent;border-bottom:3px solid transparent}
.foot-link.current{color:var(--blue)}
.info-row{left:620px;font-size:9.5px;color:var(--muted);display:flex;gap:8px;line-height:14px}
.info-row svg{flex:none;margin-top:2px}
.foot-rule{left:126px;top:1158px;width:728px;height:1px;background:var(--line)}
.copyright{left:128px;top:1169px;font-size:9.5px;color:var(--muted)}
.legal{left:747px;top:1169px;font-size:9.5px;color:var(--muted)}
</style>
</head>
<body>
<div class="abs top-rule"></div>

<header>
  <div class="abs brand"><div class="brand-mark"></div><div class="brand-name">Carrowind Auctions</div></div>

  <div class="abs follow">
    <div class="label">Follow us:</div>
    <div class="social">
      <div class="social-item"><span class="social-sq"></span>Chirpa</div>
      <div class="social-item"><span class="social-sq"></span>TradeLoop</div>
    </div>
  </div>
  <div class="abs divider-v" style="left:620px;top:40px"></div>

  <div class="abs contact-block" style="left:632px">
    <div class="label"><svg width="13" height="9" viewBox="0 0 13 9"><rect x=".5" y=".5" width="12" height="8" fill="none" stroke="#aaa"/><path d="M.5 .5 6.5 5 12.5 .5" fill="none" stroke="#aaa"/></svg>Send us an email:</div>
    <div class="contact-value">marlacarrowind@plexmail.example</div>
  </div>
  <div class="abs divider-v" style="left:810px;top:40px"></div>

  <div class="abs contact-block" style="left:822px">
    <div class="label"><svg width="10" height="10" viewBox="0 0 10 10"><path d="M2 1 4 3 3 4.5C4 6 5 7 6.5 8L8 7 10 9 8.5 10C4 9.5 .5 6 0 1.5Z" fill="#aaa"/></svg>Call us today:</div>
    <div class="contact-value phone">+(555) 904-2317</div>
  </div>
</header>

<nav class="abs main-nav">
  <div class="abs nav-item" style="left:126px">Home</div>
  <div class="abs nav-item active" style="left:176px">Auctions &#8964;</div>
  <div class="abs nav-item" style="left:277px">Online Auctions</div>
  <div class="abs nav-item" style="left:398px">About Us</div>
  <div class="abs nav-item" style="left:483px">Services</div>
  <div class="abs nav-item" style="left:563px">Real Estate Listings</div>
  <div class="abs nav-item" style="left:702px">References</div>
  <div class="abs nav-item" style="left:797px">Contact Us</div>
</nav>
<div class="abs dropdown">
  <div>Upcoming Auctions</div>
  <div class="dim">Past Auctions</div>
</div>

<section class="abs hero" role="img" aria-label="Slideshow photo of a row of suburban homes"></section>
<div class="abs slide-arrow" style="left:0"><svg width="8" height="12" viewBox="0 0 8 12"><path d="M6 1 1 6l5 5" fill="none" stroke="#fff" stroke-width="2"/></svg></div>
<div class="abs slide-arrow" style="left:947px"><svg width="8" height="12" viewBox="0 0 8 12"><path d="M2 1l5 5-5 5" fill="none" stroke="#fff" stroke-width="2"/></svg></div>

<section class="abs tagline-band">
  <h1 class="abs tagline">Since 1977, Proven Results.</h1>
  <p class="abs tagline-copy">Nulla tincidunt neque eget enim convallis auctor. Curabitur consequat molestie orci, nec malesuada ante dictum eu. Aliquam sapien tellus, elementum eget risus nec, imperdiet pellentesque urna. Lorem ipsum dolor</p>
  <div class="abs btn btn-register">Register Now</div>
</section>

<section class="abs featured">
  <div class="abs featured-photo" role="img" aria-label="Photo of the featured auction house"></div>
  <div class="abs photo-tools">
    <svg width="10" height="10" viewBox="0 0 10 10"><circle cx="4" cy="4" r="3" fill="none" stroke="#fff" stroke-width="1.5"/><path d="M6.3 6.3 9.5 9.5" stroke="#fff" stroke-width="1.5"/></svg>
    <svg width="11" height="9" viewBox="0 0 11 9"><rect x=".5" y=".5" width="10" height="8" fill="none" stroke="#fff"/><path d="M1.5 7.5 4 4.5l2 2 1.5-1.5 2 2z" fill="#fff"/></svg>
    <svg width="12" height="8" viewBox="0 0 12 8"><rect width="8" height="8" fill="#fff"/><path d="M8 4 12 1v6z" fill="#fff"/></svg>
  </div>
  <div class="abs btn btn-bidding">View Online Bidding</div>
  <h2 class="abs feat-title" style="font-weight:400">Featured Auction</h2>
  <p class="abs feat-desc">This is a test auction, for the purposes of design and functionality testing of BidWorks.example Ignite!</p>
  <div class="abs feat-loc"><svg width="7" height="10" viewBox="0 0 7 10"><path d="M3.5 0A3.5 3.5 0 0 0 0 3.5C0 6 3.5 10 3.5 10S7 6 7 3.5A3.5 3.5 0 0 0 3.5 0Z" fill="#999"/><circle cx="3.5" cy="3.5" r="1.3" fill="#fff"/></svg>P.O. BOX 41172 ROANOKE, VA 24099</div>
  <div class="abs feat-box">
    <div class="abs feat-online">ONLINE BIDDING ONLY</div>
    <div class="abs btn feat-live">LIVE OFF-SITE AUCTION</div>
    <div class="abs feat-dates">Begins:&nbsp; Tuesday, March 04, 2014 at 10:00 AM EST<br>Ends:&nbsp; Tuesday, March 11, 2014 at 11:00 PM EST</div>
  </div>
</section>

<aside>
  <h2 class="abs testimonials-title" style="font-weight:400">Testimonials</h2>
  <blockquote class="abs quote-box">"Aliquam commodo leo in quam venenatis vehicula nec eu erat. Quisque ipsum elit, interdum eu dui eget, euismod pretium ipsum."</blockquote>
  <div class="abs author">John Doe</div>
  <div class="abs author-role">Digital Marketing</div>
  <div class="abs dots"><span></span><span></span><span class="on"></span><span></span></div>
</aside>

<div class="abs partner" style="left:130px;width:56px"></div>
<div class="abs partner" style="left:220px;width:33px"></div>
<div class="abs partner" style="left:282px;width:134px"></div>
<div class="abs partner" style="left:436px;width:70px"></div>
<div class="abs partner" style="left:544px;width:162px"></div>
<div class="abs partner" style="left:740px;width:108px"></div>

<section class="abs newsletter">
  <h2 class="abs news-title" style="font-weight:400">Signup for our Newsletter</h2>
  <p class="abs news-sub">Get the latest updates and important news about the listings!</p>
  <div class="abs field" style="left:130px">Name<svg width="9" height="11" viewBox="0 0 9 11"><circle cx="4.5" cy="3" r="2.6" fill="#aaa"/><path d="M0 11C0 7 2 6 4.5 6S9 7 9 11Z" fill="#aaa"/></svg></div>
  <div class="abs field" style="left:374px">Email<svg width="13" height="9" viewBox="0 0 13 9"><rect width="13" height="9" fill="#bbb"/><path d="M0 0 6.5 5 13 0" fill="none" stroke="#fff"/></svg></div>
  <div class="abs btn btn-signup">Sign Up Now</div>
</section>

<footer>
  <h3 class="abs foot-h" style="left:130px;font-weight:400">About Carrowind Auctions</h3>
  <p class="abs foot-text">Aquam est tortor, sagittis in fringilla in, pellent esque nec erat. Aenean semper, neque non faucibus.</p>
  <div class="abs foot-social">
    <div class="social-item"><span class="social-sq"></span>Chirpa</div>
    <div class="social-item"><span class="social-sq"></span>TradeLoop</div>
  </div>

  <h3 class="abs foot-h" style="left:374px;font-weight:400">Quick Links</h3>
  <div class="abs foot-link" style="left:374px;top:1038px">Home</div>
  <div class="abs foot-link current" style="left:374px;top:1061px">Auctions</div>
  <div class="abs foot-link" style="left:374px;top:1084px">Online Auctions</div>
  <div class="abs foot-link" style="left:374px;top:1107px">About Us</div>
  <div class="abs foot-link" style="left:487px;top:1038px">Services</div>
  <div class="abs foot-link" style="left:487px;top:1061px">Real Estate Listings</div>
  <div class="abs foot-link" style="left:487px;top:1084px">References</div>
  <div class="abs foot-link" style="left:487px;top:1107px">Contact Us</div>

  <h3 class="abs foot-h" style="left:618px;font-weight:400">Contact Info</h3>
  <div class="abs info-row" style="top:1037px"><svg width="10" height="10" viewBox="0 0 10 10"><path d="M2 1 4 3 3 4.5C4 6 5 7 6.5 8L8 7 10 9 8.5 10C4 9.5 .5 6 0 1.5Z" fill="#777"/></svg>(555) 218-6049</div>
  <div class="abs info-row" style="top:1060px"><svg width="10" height="10" viewBox="0 0 10 10"><rect x="2" y=".5" width="6" height="9" rx="1" fill="none" stroke="#777"/></svg>(555) 762-3815</div>
  <div class="abs info-row" style="top:1083px"><svg width="10" height="10" viewBox="0 0 10 8"><rect x=".5" y=".5" width="9" height="7" fill="none" stroke="#777"/><path d="M.5 .5 5 4.5 9.5 .5" fill="none" stroke="#777"/></svg>marlacarrowind@plexmail.example</div>
  <div class="abs info-row" style="top:1106px"><svg width="10" height="10" viewBox="0 0 10 10"><path d="M5 0 10 5H8.5V10H6V7H4V10H1.5V5H0Z" fill="#777"/></svg>48 E. Thornbury Lane,<br>Ste 310, Pensacola, FL 32599</div>

  <div class="abs foot-rule"></div>
  <div class="abs copyright">Copyright © 2014 All Rights Reserved by Carrowind Auctions</div>
  <div class="abs legal">Privacy Policy | Sitemap</div>
</footer>
</body>
</html>
```